Wellness Coach/personal trainer Business Card Design Project

We need an eye catching logo design for a wellness coach / personal trainer who specializes in weight loss / body transformation / health coaching. We educate, empower, and support our clients on their weight loss journey. We want the look and feel described below on the business card design.

Target Market(s)

80 % women 20 % men
educated 30 - 50 women
vanity/appearance focused

Industry/Entity Type

Personal Trainer

Font styles to use
Serif

Colors
a54599
f9ed23
ffffff

Requirements
Must have
• name - Dorian Calvaske
phone - (888) 275 9146
web address - www.7PennyMover.example
tagline - Becasue Looking Good Matters
Nice to have
• see Look and Feel
Colorful, Playful, Elegant
Should not have
• no cartoons or animation

```html
<!DOCTYPE html>
<html lang="en">
<head>
<meta charset="utf-8">
<title>Dorian Calvaske – Business Cards</title>
<link rel="stylesheet" href="https://fonts.googleapis.com/css2?family=Bebas+Neue&family=Quicksand:wght@400;500&display=swap">
<style>
  :root {
    --purple: #a54599;
    --yellow: #f9ed23;
    --white: #ffffff;
    --backdrop: #2b2a2a;
  }
  * { margin: 0; padding: 0; box-sizing: border-box; }
  html, body {
    width: 1200px;
    height: 1200px;
    overflow: hidden;
    background: var(--backdrop);
  }
  .stage {
    position: relative;
    width: 1200px;
    height: 1200px;
  }
  .card {
    position: absolute;
    left: 190px;
    width: 820px;
    height: 468px;
    overflow: hidden;
  }

  /* Back of card */
  .card--back {
    top: 110px;
    background: var(--purple);
    color: var(--white);
  }
  .back-name {
    position: absolute;
    left: 72px;
    top: 78px;
    font-family: "Bebas Neue", sans-serif;
    font-size: 78px;
    font-weight: 400;
    letter-spacing: 1px;
    line-height: 1;
  }
  .contact-block {
    position: absolute;
    left: 96px;
    top: 190px;
    padding-left: 34px;
    border-left: 6px solid var(--white);
    height: 200px;
    display: flex;
    flex-direction: column;
    justify-content: center;
    gap: 16px;
  }
  .contact-row {
    display: flex;
    align-items: center;
    gap: 18px;
    font-family: "Quicksand", sans-serif;
    font-weight: 400;
    font-size: 30px;
    line-height: 1.1;
  }
  .contact-icon {
    width: 24px;
    height: 24px;
    flex: none;
    fill: var(--yellow);
  }

  /* Front of card */
  .card--front {
    top: 622px;
    background: var(--yellow);
  }
  .front-identity {
    position: absolute;
    left: 50px;
    top: 84px;
    width: 330px;
  }
  .front-name {
    font-family: "Bebas Neue", sans-serif;
    font-size: 96px;
    font-weight: 400;
    line-height: 0.86;
    color: var(--purple);
    letter-spacing: 1px;
  }
  .front-role {
    margin-top: 20px;
    font-family: "Bebas Neue", sans-serif;
    font-size: 32px;
    line-height: 1;
    color: var(--white);
    letter-spacing: 0.5px;
  }
  .divider {
    position: absolute;
    left: 396px;
    top: 50px;
    width: 7px;
    height: 370px;
    background: var(--white);
  }
  .figure-area {
    position: absolute;
    left: 410px;
    top: 70px;
    width: 110px;
    height: 330px;
    border-radius: 40px 40px 8px 8px;
    background: linear-gradient(180deg, #b053a4 0%, var(--purple) 100%);
  }
  .tagline {
    position: absolute;
    left: 540px;
    top: 84px;
    font-family: "Bebas Neue", sans-serif;
    font-size: 82px;
    line-height: 0.9;
    color: var(--white);
    letter-spacing: 1px;
  }
</style>
</head>
<body>
<main class="stage">

  <section class="card card--back" aria-label="Business card back">
    <h1 class="back-name">Dorian Calvaske</h1>
    <div class="contact-block">
      <p class="contact-row">
        <svg class="contact-icon" viewBox="0 0 24 24" aria-hidden="true">
          <circle cx="12" cy="7" r="5"/>
          <path d="M3 24c0-6 4-9 9-9s9 3 9 9z"/>
        </svg>
        Wellness Coach &amp; Personal Trainer
      </p>
      <p class="contact-row">
        <svg class="contact-icon" viewBox="0 0 24 24" aria-hidden="true">
          <path d="M6.6 10.8a15 15 0 0 0 6.6 6.6l2.2-2.2a1 1 0 0 1 1-.25 11.4 11.4 0 0 0 3.6.57 1 1 0 0 1 1 1V20a1 1 0 0 1-1 1A17 17 0 0 1 3 4a1 1 0 0 1 1-1h3.5a1 1 0 0 1 1 1c0 1.25.2 2.45.57 3.57a1 1 0 0 1-.25 1z"/>
        </svg>
        (888) 275 9146
      </p>
      <p class="contact-row">
        <svg class="contact-icon" viewBox="0 0 24 24" aria-hidden="true">
          <path d="M12 2a10 10 0 1 0 0 20 10 10 0 0 0 0-20zm6.9 6h-2.9a15.6 15.6 0 0 0-1.4-3.6A8 8 0 0 1 18.9 8zM12 4c.8 1.2 1.5 2.5 1.9 4h-3.8c.4-1.5 1.100-2.8 1.9-4zM4.3 14a8 8 0 0 1 0-4h3.4a16 16 0 0 0 0 4zm.8 2h2.9c.3 1.3.8 2.5 1.4 3.6A8 8 0 0 1 5.1 16zM8 8H5.1a8 8 0 0 1 4.3-3.6C8.8 5.5 8.3 6.7 8 8zm4 12c-.8-1.2-1.5-2.5-1.9-4h3.8c-.4 1.5-1.1 2.8-1.9 4zm2.3-6H9.7a14.6 14.6 0 0 1 0-4h4.6a14.6 14.6 0 0 1 0 4zm.3 5.6c.6-1.1 1.1-2.3 1.4-3.6h2.9a8 8 0 0 1-4.3 3.6zm1.7-5.6a16 16 0 0 0 0-4h3.4a8 8 0 0 1 0 4z"/>
        </svg>
        www.7PennyMover.example
      </p>
    </div>
  </section>

  <section class="card card--front" aria-label="Business card front">
    <div class="front-identity">
      <h2 class="front-name">Dorian<br>Calvaske</h2>
      <p class="front-role">Wellness Coach<br>&amp; Personal Trainer</p>
    </div>
    <div class="divider"></div>
    <div class="figure-area" role="img" aria-label="Purple silhouette of a confident woman standing with hands on hips"></div>
    <p class="tagline">Because<br>Looking<br>Good<br>Matters</p>
  </section>

</main>
</body>
</html>
```